Facebook post - Tidy Joint Crew has arrived to make your tiles smile!

Tidy Joint Crew would like to release a Facebook post calling out to the market that we have arrived. The company has a new and fresh branding aiming for a female demographic between the ages of 40 and 55 located in the South West of Western Australia. The company image MUST be centered around trust! Our Primary aim is to create an uncompromising trust from the very first impression. Our logo tag line is, 'We love to make your tiles smile'.
I need 5 x facebook template designs and also 5 x posts.
Our 1st campaign is to be 5 x posts centered around the arrival of this fantastic new company.
We are company that provides the services of:
- Grout and silicone repair.
- Broken or drummy tile replacement and;
- Grout sealing
Dont forget that we must communicate TRUST and the we love to make your tiles SMILE!

```html
<!DOCTYPE html>
<html lang="en">
<head>
<meta charset="utf-8">
<title>Tidy Joint Crew – Facebook Post</title>
<link href="https://fonts.googleapis.com/css2?family=Montserrat:wght@400;500;600;700;800&display=swap" rel="stylesheet">
<style>
  :root {
    --blue: #1e9ad6;
    --blue-deep: #0f78b8;
    --blue-light: #d7eef9;
    --ink: #1f2a33;
    --white: #ffffff;
    --board-light: #ffffff;
    --board-dark: #14495b;
    --photo-a: #c9d6df;
    --photo-b: #8fa5b4;
  }
  * { margin: 0; padding: 0; box-sizing: border-box; }
  html, body { width: 1200px; height: 2400px; overflow: hidden; }
  body { font-family: "Montserrat", Arial, sans-serif; color: var(--ink); }
  .board { position: absolute; left: 0; width: 1200px; }
  .board--light { top: 0; height: 1240px; background: var(--board-light); }
  .board--dark { top: 1240px; height: 1160px; background: var(--board-dark); }
  .post {
    position: absolute; left: 88px; width: 1024px; height: 1024px;
    background: var(--white); overflow: hidden;
    box-shadow: 0 6px 20px rgba(0,0,0,.18);
  }
  .board--light .post { top: 40px; }
  .board--dark .post { top: 96px; }
  .post__shape { position: absolute; inset: 0; }

  .brand { position: absolute; left: 40px; top: 150px; width: 330px; text-align: center; }
  .brand__dot { width: 46px; height: 46px; border-radius: 50%; background: var(--blue); margin: 0 auto 14px; }
  .brand__name { font-weight: 800; font-size: 30px; color: var(--blue-deep); letter-spacing: .5px; }
  .brand__tagline { font-size: 12px; font-weight: 600; color: var(--blue); letter-spacing: 1px; margin-top: 4px; }

  .photo {
    position: absolute; left: 120px; top: 330px; width: 450px; height: 450px;
    border-radius: 50%; border: 12px solid var(--blue);
    background: radial-gradient(circle at 40% 40%, var(--photo-a), var(--photo-b));
  }
  .photo--small {
    left: 40px; top: 300px; width: 150px; height: 150px; border-width: 8px;
    background: radial-gradient(circle at 50% 40%, #e4ecf1, #a9bac6);
  }
  .badge {
    position: absolute; left: 60px; top: 580px; width: 120px; height: 120px;
    border-radius: 50%; background: var(--white); border: 6px solid var(--blue);
    display: flex; align-items: center; justify-content: center;
    font-weight: 800; font-size: 36px; color: var(--blue-deep);
  }
  .emergency {
    position: absolute; left: 360px; top: 650px; width: 260px; padding: 12px 18px;
    background: rgba(255,255,255,.92);
    font-weight: 800; font-size: 30px; line-height: 1.08; color: var(--ink);
  }

  .headline {
    position: absolute; left: 580px; top: 100px; width: 420px;
    color: var(--white); text-align: right; white-space: nowrap;
  }
  .headline__top { font-size: 54px; font-weight: 500; line-height: 1.05; }
  .headline__top b { font-weight: 800; }
  .headline__main { font-size: 54px; font-weight: 800; line-height: 1.05; }
  .tagline-bar {
    position: absolute; left: 590px; top: 232px; width: 410px; padding: 6px 10px;
    background: var(--white); color: var(--blue-deep);
    font-size: 16px; font-weight: 700; text-align: center; white-space: nowrap;
  }
  .intro { position: absolute; left: 650px; top: 282px; width: 340px; color: var(--white); font-size: 18px; font-weight: 500; line-height: 1.3; text-align: center; }

  .services { position: absolute; left: 640px; top: 470px; width: 360px; color: var(--white); }
  .services__title { font-size: 26px; font-weight: 500; margin-bottom: 12px; }
  .services__title b { font-weight: 800; }
  .service {
    display: flex; align-items: center; justify-content: space-between;
    border-top: 2px solid rgba(255,255,255,.5); padding: 14px 0;
    font-size: 18px; font-weight: 500; line-height: 1.2;
  }
  .service b { font-weight: 800; }
  .service__icon { width: 46px; height: 46px; flex: none; }

  .call { position: absolute; left: 640px; top: 872px; width: 360px; color: var(--white); font-size: 26px; font-weight: 500; text-align: right; }
  .call b { font-weight: 800; }
  .phone {
    position: absolute; left: 640px; top: 912px; width: 360px; padding: 6px 0;
    background: var(--white); color: var(--ink); text-align: center;
    font-size: 40px; font-weight: 700;
  }

  .contact { position: absolute; left: 40px; top: 820px; width: 520px; }
  .contact__title { font-size: 26px; font-weight: 800; margin-bottom: 10px; }
  .contact__line { display: flex; align-items: center; gap: 12px; font-size: 17px; font-weight: 500; margin-bottom: 6px; }
  .contact__icon { width: 22px; height: 22px; border-radius: 4px; background: var(--blue); flex: none; }
</style>
</head>
<body>

<section class="board board--light">
  <article class="post">
    <svg class="post__shape" viewBox="0 0 1024 1024" aria-hidden="true">
      <path d="M380 0 C 300 40, 250 120, 160 130 C 230 60, 300 20, 330 0 Z" fill="var(--blue-light)"/>
      <path d="M400 0 H1024 V1024 H0 V990 C180 950 380 1010 590 975 C640 880 610 760 620 640 C560 560 540 420 610 320 C500 260 420 150 400 0 Z" fill="var(--blue)"/>
      <path d="M0 1004 C200 970 420 1024 620 990 L1024 1000 V1024 H0 Z" fill="var(--blue-deep)"/>
    </svg>
    <div class="brand">
      <div class="brand__dot"></div>
      <div class="brand__name">TIDY JOINT CREW</div>
      <div class="brand__tagline">WE LOVE TO MAKE YOUR TILES SMILE</div>
    </div>
    <div class="photo" role="img" aria-label="Photo of a tiler repairing grout on a bathroom floor"></div>
    <div class="photo photo--small" role="img" aria-label="Photo of freshly grouted tiles"></div>
    <div class="badge">24/7</div>
    <div class="emergency">EMERGENCY<br>WATER<br>REMOVAL</div>
    <div class="headline">
      <div class="headline__top"><b>LETS</b> YOU</div>
      <div class="headline__main">LIVE BETTER</div>
    </div>
    <div class="tagline-bar">WE LOVE TO MAKE YOUR TILES SMILE</div>
    <p class="intro">Come home to see quality tiles and we also provide emergency removal and 24x7 flood response.</p>
    <div class="services">
      <div class="services__title">OUR <b>SERVICES</b></div>
      <div class="service"><span><b>GROUT</b> AND<br><b>SILICONE REPAIR</b></span>
        <svg class="service__icon" viewBox="0 0 46 46"><circle cx="23" cy="23" r="21" fill="none" stroke="#fff" stroke-width="2.5"/><path d="M14 24 l6 6 l12 -13" fill="none" stroke="#fff" stroke-width="3"/></svg></div>
      <div class="service"><span>BROKEN OR <b>DRUMMY</b><br><b>TILE</b> REPLACEMENT.</span>
        <svg class="service__icon" viewBox="0 0 46 46"><circle cx="23" cy="23" r="21" fill="none" stroke="#fff" stroke-width="2.5"/><rect x="14" y="14" width="18" height="18" fill="none" stroke="#fff" stroke-width="2.5"/><path d="M23 14 V32 M14 23 H32" stroke="#fff" stroke-width="2"/></svg></div>
      <div class="service"><span>GROUT <b>SEALING.</b></span>
        <svg class="service__icon" viewBox="0 0 46 46"><circle cx="23" cy="23" r="21" fill="none" stroke="#fff" stroke-width="2.5"/><path d="M16 30 L30 16 M20 32 L32 20" stroke="#fff" stroke-width="3"/></svg></div>
    </div>
    <div class="call">CALL <b>NOW:</b></div>
    <div class="phone">0400 118 274</div>
    <div class="contact">
      <div class="contact__title">CONTACT:</div>
      <div class="contact__line"><span class="contact__icon"></span>hello@tidyjointcrew.com.au</div>
      <div class="contact__line"><span class="contact__icon"></span>www.tidyjointcrew.com.au</div>
      <div class="contact__line"><span class="contact__icon"></span>PO Box 1187, Cowrie Bay WA 6290</div>
    </div>
  </article>
</section>

<section class="board board--dark">
  <article class="post">
    <svg class="post__shape" viewBox="0 0 1024 1024" aria-hidden="true">
      <path d="M380 0 C 300 40, 250 120, 160 130 C 230 60, 300 20, 330 0 Z" fill="var(--blue-light)"/>
      <path d="M400 0 H1024 V1024 H0 V990 C180 950 380 1010 590 975 C640 880 610 760 620 640 C560 560 540 420 610 320 C500 260 420 150 400 0 Z" fill="var(--blue)"/>
      <path d="M0 1004 C200 970 420 1024 620 990 L1024 1000 V1024 H0 Z" fill="var(--blue-deep)"/>
    </svg>
    <div class="brand">
      <div class="brand__dot"></div>
      <div class="brand__name">TIDY JOINT CREW</div>
      <div class="brand__tagline">WE LOVE TO MAKE YOUR TILES SMILE</div>
    </div>
    <div class="photo" role="img" aria-label="Photo of a tiler repairing grout on a bathroom floor"></div>
    <div class="photo photo--small" role="img" aria-label="Photo of freshly grouted tiles"></div>
    <div class="badge">24/7</div>
    <div class="emergency">EMERGENCY<br>WATER<br>REMOVAL</div>
    <div class="headline">
      <div class="headline__top"><b>LETS</b> YOU</div>
      <div class="headline__main">LIVE BETTER</div>
    </div>
    <div class="tagline-bar">WE LOVE TO MAKE YOUR TILES SMILE</div>
    <p class="intro">Come home to see quality tiles and we also provide emergency removal and 24x7 flood response.</p>
    <div class="services">
      <div class="services__title">OUR <b>SERVICES</b></div>
      <div class="service"><span><b>GROUT</b> AND<br><b>SILICONE REPAIR</b></span>
        <svg class="service__icon" viewBox="0 0 46 46"><circle cx="23" cy="23" r="21" fill="none" stroke="#fff" stroke-width="2.5"/><path d="M14 24 l6 6 l12 -13" fill="none" stroke="#fff" stroke-width="3"/></svg></div>
      <div class="service"><span>BROKEN OR <b>DRUMMY</b><br><b>TILE</b> REPLACEMENT.</span>
        <svg class="service__icon" viewBox="0 0 46 46"><circle cx="23" cy="23" r="21" fill="none" stroke="#fff" stroke-width="2.5"/><rect x="14" y="14" width="18" height="18" fill="none" stroke="#fff" stroke-width="2.5"/><path d="M23 14 V32 M14 23 H32" stroke="#fff" stroke-width="2"/></svg></div>
      <div class="service"><span>GROUT <b>SEALING.</b></span>
        <svg class="service__icon" viewBox="0 0 46 46"><circle cx="23" cy="23" r="21" fill="none" stroke="#fff" stroke-width="2.5"/><path d="M16 30 L30 16 M20 32 L32 20" stroke="#fff" stroke-width="3"/></svg></div>
    </div>
    <div class="call">CALL <b>NOW:</b></div>
    <div class="phone">0400 118 274</div>
    <div class="contact">
      <div class="contact__title">CONTACT:</div>
      <div class="contact__line"><span class="contact__icon"></span>hello@tidyjointcrew.com.au</div>
      <div class="contact__line"><span class="contact__icon"></span>www.tidyjointcrew.com.au</div>
      <div class="contact__line"><span class="contact__icon"></span>PO Box 1187, Cowrie Bay WA 6290</div>
    </div>
  </article>
</section>

</body>
</html>
```